4 page website for our new business,
www.Ridge Crest Bathrooms.example
We will provide the follwing service
1st Home page, bathroom renvovations, make over redesign etc
2nd page Tiling service
3rd page Waterproofing
4th page Galllery
The home will maily focus on the core business bathroom renovation, customer should able request quote, via entering thier info eg. name and contact number and select the 3 services
Need area for testimonials that will scroll
Maybe a banner which may flash varies pic of different design
Maybe a area for giving reasons why customer should go with us for they job
simple site which will grentrate leads, create presece, build brand.
We've just had the logo design, which allow you to create theme.
Target Market(s)
home owner's mum and dad
Look and feel

```html
<!DOCTYPE html>
<html lang="en">
<head>
<meta charset="utf-8">
<title>Ridge Crest Bathrooms – Tilling Service</title>
<link href="https://fonts.googleapis.com/css2?family=Oswald:wght@300;400;500;600&family=Arimo:wght@400;700&display=swap" rel="stylesheet">
<style>
:root{
  --backdrop:#e6e6e6;
  --page:#f4f4f4;
  --panel:#e3e3e3;
  --ink:#222;
  --text:#8a8a8a;
  --muted:#666;
  --accent:#3f95d8;
  --pill-dark:#3a3a3a;
  --line:#cfcfcf;
  --footer:#474747;
  --footer-text:#d8d8d8;
  --tick:#3c9a22;
  --logo:#3b3b3b;
}
*{box-sizing:border-box;margin:0;padding:0}
html,body{width:1200px;height:2211px;overflow:hidden}
body{background:var(--backdrop);font-family:"Arimo",Arial,sans-serif;color:var(--text);position:relative}
.abs{position:absolute}
.page{left:124px;top:96px;width:954px;height:2015px;background:var(--page);border-radius:6px 6px 0 0}
h1,h2,h3,h4{font-family:"Oswald",sans-serif;color:var(--ink);font-weight:500}
.search{left:833px;top:109px;width:206px;height:21px;border:1px solid #c6c6c6;border-radius:11px;background:#fff;font-size:11px;color:#aaa;padding:4px 12px;line-height:12px}
.search .btn{position:absolute;right:-1px;top:-1px;width:24px;height:21px;border-radius:11px;background:#ececec;border:1px solid #c6c6c6}
.logo{left:177px;top:155px;display:flex;align-items:center;gap:10px;font-size:27px;color:var(--logo);font-weight:400;white-space:nowrap}
.logo .mark{width:16px;height:16px;border-radius:50%;background:#f0a22a}
.nav{left:596px;top:169px;display:flex;gap:7px}
.pill{height:22px;border:1px solid #bdbdbd;border-radius:12px;background:linear-gradient(#fff,#e8e8e8);font-size:11px;color:#444;padding:0 9px;line-height:20px;white-space:nowrap}
.pill.active{background:var(--pill-dark);color:#fff;border-color:#222}
.titlebar{left:149px;top:242px;width:900px;height:41px;background:#e2e2e2;padding:7px 12px}
.titlebar h1{font-size:21px;font-weight:600;line-height:27px}
.crumb{right:161px;top:287px;font-size:11px;color:var(--muted);white-space:nowrap}
.crumb span{color:var(--accent)}
.side-menu{left:149px;top:317px;width:217px}
.side-menu li{list-style:none;height:31px;margin-bottom:5px;border:1px solid #c2c2c2;border-radius:16px;background:linear-gradient(#fff,#e9e9e9);font-size:11.5px;color:#444;padding:0 16px;line-height:29px;white-space:nowrap}
.side-menu li.active{background:linear-gradient(#5a5a5a,#2f2f2f);color:#fff;border-color:#222}
.news{left:149px;top:528px;width:217px;height:496px;background:var(--panel);padding:8px 8px 0}
.news h3{font-size:16px;margin-bottom:12px}
.news-item{border-bottom:1px solid #f7f7f7;padding:0 2px 12px;margin-bottom:12px;height:151px}
.news-item:last-child{border:0}
.news-item b{display:block;font-size:11px;line-height:17px;color:#333;margin-bottom:14px}
.news-item p{font-size:11px;line-height:17px}
.more{display:flex;align-items:center;justify-content:center;gap:6px;height:22px;border:1px solid #bdbdbd;border-radius:12px;background:linear-gradient(#fff,#e8e8e8);font-size:11px;color:#444;padding:0 9px 0 11px;width:auto;min-width:84px;white-space:nowrap}
.more svg{flex-shrink:0}
.news-item .more,.service .more{width:max-content;margin:6px 0 0 auto}
.newsletter{left:159px;top:1070px;width:208px}
.newsletter h3,.contact h3{font-size:16px;margin-bottom:6px}
.newsletter b{font-size:11px;line-height:17px;color:#333;display:block;margin-bottom:18px}
.field{height:28px;border:1px solid #c8c8c8;border-radius:14px 0 0 14px;background:linear-gradient(#e9e9e9,#fff);font-size:11px;color:#999;padding:0 11px;line-height:26px;margin-bottom:8px}
.newsletter .more{margin:0 0 0 auto;width:84px;height:25px}
.newsletter hr{border:0;border-top:1px solid #c8c8c8;margin-top:9px}
.contact{left:159px;top:1284px;width:200px;font-size:11px;color:#555;line-height:18px}
.map{width:183px;height:82px;margin:6px 0 10px 9px;background:linear-gradient(135deg,#e9e3cf,#c8d8e3 60%,#e8e4d5);border:1px solid #ddd}
.contact .addr{padding-left:7px}
.contact .phone{font-size:15px;color:#222;font-weight:700;line-height:20px;margin-top:4px}
.main{left:385px;top:313px;width:654px}
.main h2{font-size:22px}
.main p{font-size:11px;line-height:16.5px}
.photo{background:linear-gradient(180deg,#5a5440 0%,#d9c9a5 40%,#a86a3c 75%,#7a4a2c);border-radius:6px}
.divider{height:1px;background:#c8c8c8;box-shadow:0 6px 10px rgba(0,0,0,.06)}
.sub{font-family:"Oswald",sans-serif;font-weight:400;color:var(--accent);font-size:16px}
.checks{display:grid;grid-template-columns:273px 273px;row-gap:11px;margin:18px 0 0 75px}
.checks li{list-style:none;font-size:11px;display:flex;align-items:center;gap:10px;white-space:nowrap}
.work{border-radius:5px}
.caption{font-size:11px;color:#444;white-space:nowrap}
.caption b{color:#222}
.service h4{font-size:16px;margin:16px 0 6px}
.service p{font-size:11px;line-height:16px;color:#9a9a9a}
.service .more{margin-top:16px}
.footer{left:124px;top:1853px;width:954px;height:258px;background:var(--footer);border-radius:0 0 6px 6px;box-shadow:inset 0 6px 6px rgba(0,0,0,.25)}
.fcol{position:absolute;top:30px;width:200px}
.fcol h4{font-family:"Oswald",sans-serif;font-weight:300;color:#eee;font-size:16px;margin-bottom:8px}
.fcol li{list-style:none;font-size:11px;color:var(--footer-text);height:34px;line-height:34px;padding-left:10px;border-bottom:1px dotted #777;white-space:nowrap}
.fcol li.big{font-size:15px}
.social{left:570px;top:2126px;display:flex;gap:6px}
.social span{width:18px;height:18px;background:#555;border:1px solid #333;border-radius:2px}
.copy{left:0;top:2164px;width:1200px;text-align:center;font-size:11px;color:#777}
</style>
</head>
<body>
<div class="abs page"></div>

<header>
  <div class="abs search">search...<span class="btn"></span></div>
  <div class="abs logo"><span class="mark"></span>Ridge Crest Bathrooms</div>
  <nav class="abs nav">
    <span class="pill">Home</span>
    <span class="pill">Renovation</span>
    <span class="pill active">Tilling service</span>
    <span class="pill">Waterproofing</span>
    <span class="pill">Gallery</span>
    <span class="pill">Contact</span>
  </nav>
</header>

<div class="abs titlebar"><h1>Tilling Service</h1></div>
<div class="abs crumb">You at here: Home &gt; Tilling Service &gt; <span>About tilling service</span></div>

<aside>
  <ul class="abs side-menu">
    <li class="active">About Tilling Service</li>
    <li>Our Team</li>
    <li>Recent Project</li>
    <li>Our Client</li>
    <li>Testimonial</li>
  </ul>

  <section class="abs news">
    <h3>Latest news</h3>
    <div class="news-item"><b>Duis autem vel eum iriure dolor in hendrerit in vulputate.</b><p>Velit esse molestie consequat, vel illum dolore eu feugiat nulla facilisis. At vero eos et accusam et justo duo.</p><div class="more">Read more <svg width="10" height="8"><path d="M0 3h6V0l4 4-4 4V5H0z" fill="#3f95d8"/></svg></div></div>
    <div class="news-item"><b>Duis autem vel eum iriure dolor in hendrerit in vulputate.</b><p>Velit esse molestie consequat, vel illum dolore eu feugiat nulla facilisis. At vero eos et accusam et justo duo.</p><div class="more">Read more <svg width="10" height="8"><path d="M0 3h6V0l4 4-4 4V5H0z" fill="#3f95d8"/></svg></div></div>
    <div class="news-item"><b>Duis autem vel eum iriure dolor in hendrerit in vulputate.</b><p>Velit esse molestie consequat, vel illum dolore eu feugiat nulla facilisis. At vero eos et accusam et justo duo.</p><div class="more">Read more <svg width="10" height="8"><path d="M0 3h6V0l4 4-4 4V5H0z" fill="#3f95d8"/></svg></div></div>
  </section>

  <section class="abs newsletter">
    <h3>Newsletter</h3>
    <b>Duis autem vel eum iriure dolor in hendrerit in vulputate.</b>
    <div class="field">Your name</div>
    <div class="field">Your email</div>
    <div class="more">Submit <svg width="10" height="8"><path d="M0 3h6V0l4 4-4 4V5H0z" fill="#3f95d8"/></svg></div>
    <hr>
  </section>

  <section class="abs contact">
    <h3>Contact</h3>
    <div class="map" role="img" aria-label="Street map showing the showroom location"></div>
    <div class="addr">27 A Sample Streets here<br>Sample City - Sample Country
      <div class="phone">+888-555-0142</div>
      <div style="line-height:12px">info@ridgecrest.example</div>
    </div>
  </section>
</aside>

<main>
  <section class="abs main">
    <h2>About Tilling Service</h2>
    <p style="margin-top:6px">Lorem ipsum dolor sit amet, consetetur sadipscing elitr, sed diam nonumy eirmod tempor invidunt ut labore et dolore magna aliquyam erat, sed diam voluptua. At vero eos et accusam et justo duo dolores et ea rebum. Stet clita kasd gubergren, no sea takimata sanctus est Lorem ipsum dolor sit amet. Lorem ipsum dolor sit amet, consetetur sadipscing elitr, sed diam nonumy eirmod tempor invidunt ut labore et dolore magna aliquyam erat, sed diam voluptua.</p>
    <div class="photo" style="height:199px;margin-top:12px" role="img" aria-label="Tiler laying floor tiles in a bright room"></div>
    <p style="margin-top:18px">Lorem ipsum dolor sit amet, consetetur sadipscing elitr, sed diam nonumy eirmod tempor invidunt ut labore et dolore magna aliquyam erat, sed diam voluptua. At vero eos et accusam et justo duo dolores et ea rebum. Stet clita kasd gubergren, no sea takimata sanctus est Lorem ipsum dolor sit amet. Lorem ipsum dolor sit amet, consetetur sadipscing elitr, sed diam nonumy eirmod tempor invidunt ut labore et dolore magna aliquyam erat, sed diam voluptua.</p>
    <div class="divider" style="margin:29px 44px 0 72px"></div>

    <h2 style="margin-top:30px">Why Choose Us?</h2>
    <div class="sub">The better choice</div>
    <p style="margin-top:2px">Ut wisi enim ad minim veniam, quis nostrud exerci tation ullamcorper suscipit lobortis nisl ut aliquip ex ea commodo consequat. Nam liber tempor cum soluta. Nobis eleifend option congue nihil. Doming id quod mazim.</p>
    <ul class="checks">
      <li><svg width="12" height="11"><path d="M1 6l3 3 7-8" stroke="#3c9a22" stroke-width="2.4" fill="none"/></svg>Nam liber tempor cum soluta.</li>
      <li><svg width="12" height="11"><path d="M1 6l3 3 7-8" stroke="#3c9a22" stroke-width="2.4" fill="none"/></svg>Nam liber tempor cum soluta.</li>
      <li><svg width="12" height="11"><path d="M1 6l3 3 7-8" stroke="#3c9a22" stroke-width="2.4" fill="none"/></svg>Nobis eleifend option congue nihil.</li>
      <li><svg width="12" height="11"><path d="M1 6l3 3 7-8" stroke="#3c9a22" stroke-width="2.4" fill="none"/></svg>Nobis eleifend option congue nihil.</li>
      <li><svg width="12" height="11"><path d="M1 6l3 3 7-8" stroke="#3c9a22" stroke-width="2.4" fill="none"/></svg>Doming id quod mazim.</li>
      <li><svg width="12" height="11"><path d="M1 6l3 3 7-8" stroke="#3c9a22" stroke-width="2.4" fill="none"/></svg>Doming id quod mazim.</li>
      <li><svg width="12" height="11"><path d="M1 6l3 3 7-8" stroke="#3c9a22" stroke-width="2.4" fill="none"/></svg>Lorem ipsum dolor sit amet.</li>
      <li><svg width="12" height="11"><path d="M1 6l3 3 7-8" stroke="#3c9a22" stroke-width="2.4" fill="none"/></svg>Lorem ipsum dolor sit amet.</li>
    </ul>
    <div class="divider" style="margin:26px 44px 0 72px"></div>
    <h2 style="margin-top:20px">Our Work</h2>
  </section>

  <div class="abs work" style="left:386px;top:1077px;width:282px;height:155px;background:linear-gradient(180deg,#6b5038,#d8cfc0 55%,#2a2a2a 80%,#ddd)" role="img" aria-label="Bathroom with freestanding tub on checkered floor"></div>
  <div class="abs work" style="left:759px;top:1077px;width:283px;height:155px;background:linear-gradient(135deg,#b68d3a,#8e4b3a 45%,#3c7fa8 80%,#4c9ec0)" role="img" aria-label="Close-up of coloured textured tiles"></div>
  <div class="abs caption" style="left:389px;top:1243px">Project 1: <b>Bathroom tile</b></div>
  <div class="abs caption" style="left:762px;top:1243px">Project 2: <b>Experimental</b></div>
  <div class="abs work" style="left:386px;top:1296px;width:282px;height:153px;background:linear-gradient(160deg,#8a8a8a,#3f4249 45%,#2d3036)" role="img" aria-label="Dark floor tiles with inset step lights"></div>
  <div class="abs work" style="left:759px;top:1296px;width:283px;height:153px;background:linear-gradient(180deg,#c79a6a,#ead6be 50%,#b07a4e)" role="img" aria-label="Warm-toned bathroom with wooden tub"></div>
  <div class="abs caption" style="left:389px;top:1459px">Project 3: <b>Bathroom tile</b></div>
  <div class="abs caption" style="left:762px;top:1459px">Project 4: <b>Experimental</b></div>

  <div class="abs divider" style="left:192px;top:1503px;width:815px"></div>

  <section class="abs service" style="left:159px;top:1546px;width:282px">
    <div class="work" style="height:134px;background:linear-gradient(90deg,#2a2a22,#a7b52a 40%,#c7cf3a 70%,#3a3a30)" role="img" aria-label="Modern lime green bathroom design"></div>
    <h4>Design Services</h4>
    <p>Duis autem vel eum iriure dolor in hendrerit in vulputate velit esse molestie consequat, vel illum dolore eu feugiat. nulla facilisis at vero eros et accumsan.</p>
    <div class="more">Read more <svg width="10" height="8"><path d="M0 3h6V0l4 4-4 4V5H0z" fill="#3f95d8"/></svg></div>
  </section>
  <section class="abs service" style="left:460px;top:1546px;width:281px">
    <div class="work" style="height:134px;background:linear-gradient(180deg,#cfc2ae,#a8774a 55%,#7a5a3a)" role="img" aria-label="Bathroom under renovation with timber framing"></div>
    <h4>Renovation</h4>
    <p>Duis autem vel eum iriure dolor in hendrerit in vulputate velit esse molestie consequat, vel illum dolore eu feugiat. nulla facilisis at vero eros et accumsan.</p>
    <div class="more">Read more <svg width="10" height="8"><path d="M0 3h6V0l4 4-4 4V5H0z" fill="#3f95d8"/></svg></div>
  </section>
  <section class="abs service" style="left:759px;top:1546px;width:283px">
    <div class="work" style="height:134px;background:linear-gradient(180deg,#efefef 0%,#e6e6ea 40%,#5a4f7a 55%,#4a4068)" role="img" aria-label="Made-over bathroom with purple walls and clawfoot tub"></div>
    <h4>Make Over</h4>
    <p>Duis autem vel eum iriure dolor in hendrerit in vulputate velit esse molestie consequat, vel illum dolore eu feugiat. nulla facilisis at vero eros et accumsan.</p>
    <div class="more">Read more <svg width="10" height="8"><path d="M0 3h6V0l4 4-4 4V5H0z" fill="#3f95d8"/></svg></div>
  </section>
</main>

<footer class="abs footer">
  <div class="fcol" style="left:38px"><h4>Site Map</h4><ul><li>Home</li><li>Renovation</li><li>Tilling Services</li><li>Waterproofing</li><li>Gallery</li></ul></div>
  <div class="fcol" style="left:262px"><h4>Our Company</h4><ul><li>About Us</li><li>Terms &amp; Condition</li><li>Privacy Policy</li><li>Contact Us</li></ul></div>
  <div class="fcol" style="left:486px"><h4>Our Services</h4><ul><li>Design &amp; Consultant Project</li><li>Bathroom Renovations</li><li>Bathroom Make Over</li><li>Product &amp; Selling</li></ul></div>
  <div class="fcol" style="left:712px"><h4>Contact Us</h4><ul><li>27 A Sample Streets here</li><li>Sample City - Sample Country</li><li class="big">+888-555-0142</li><li class="big">info@ridgecrest.example</li></ul></div>
</footer>

<div class="abs social"><span></span><span></span><span></span></div>
<div class="abs copy">Ridge Crest Bathrooms © 2012 - All Right Reserved</div>
</body>
</html>
```